Talbrin Business Cards

Front and back. Simon Kavelle MBA is the CEO of Talbrin Homes. Black white and grays. Logo and cool design.

Target Market(s)

Professional lenders and investors

Industry/Entity Type

Real estate developer. NO HOUSES OR ROOFS

Contact Information for Business Card

Logo, name and unique design. Front and back. Simon Kavelle MBA is the CEO of Talbrin Homes. Black white and grays. Logo and cool design.

Font styles to use
Sans Serif

Colors

Designer to choose only greyscale colors for use in the design.

Requirements
Must have
• Cool look. Not the same card I could design.
Nice to have
• Something memorable
Should not have
• Basic

```html
<!DOCTYPE html>
<html lang="en">
<head>
<meta charset="utf-8">
<title>Talbrin Business Cards</title>
<link href="https://fonts.googleapis.com/css2?family=Roboto:wght@400;700;900&display=swap" rel="stylesheet">
<style>
  :root {
    --backdrop: #3b3b3b;
    --card: #232323;
    --card-edge: #4a4a4a;
    --ink: #f2f2f2;
    --ink-soft: #d6d6d6;
    --gloss: #6e6e6e;
    --divider: #5a5a5a;
  }
  * { margin: 0; padding: 0; box-sizing: border-box; }
  html, body {
    width: 1200px; height: 793px; overflow: hidden;
    background: var(--backdrop);
    font-family: "Roboto", Arial, sans-serif;
  }
  .stage {
    position: relative; width: 1200px; height: 793px;
    display: flex; align-items: center; justify-content: center; gap: 50px;
  }
  .card {
    position: relative; width: 520px; height: 298px;
    background: var(--card);
    border: 1px solid var(--card-edge);
    box-shadow: 0 18px 40px rgba(0,0,0,.45);
  }
  .card-front { display: flex; align-items: center; }
  .front-brand {
    width: 270px; display: flex; justify-content: center;
  }
  .brand-name {
    font-weight: 900; font-size: 40px; color: var(--ink);
    letter-spacing: -1px; white-space: nowrap;
  }
  .divider {
    width: 1px; height: 190px; background: var(--divider);
  }
  .contact { padding-left: 26px; color: var(--ink-soft); font-size: 12.5px; line-height: 1.45; }
  .contact-name { font-weight: 700; font-size: 16px; color: var(--ink); }
  .contact-role { margin-bottom: 10px; }
  .contact-address { margin-bottom: 10px; }
  .contact-line { display: flex; align-items: center; gap: 8px; }
  .contact-line svg { width: 11px; height: 11px; flex: none; }
  .card-back { display: flex; align-items: center; justify-content: center; }
  .card-back .brand-name { font-size: 54px; color: var(--gloss); }
</style>
</head>
<body>
<main class="stage">
  <section class="card card-front">
    <div class="front-brand"><span class="brand-name">Talbrin Homes</span></div>
    <div class="divider"></div>
    <div class="contact">
      <div class="contact-name">Simon Kavelle MBA</div>
      <div class="contact-role">CEO</div>
      <div class="contact-address">4120 Larkspur Way<br>Northgate, Ventra 60218</div>
      <div class="contact-line">
        <svg viewBox="0 0 12 12"><path d="M2 1h3l1 3-2 1a7 7 0 0 0 3 3l1-2 3 1v3c-6 1-10-3-9-9z" fill="#f2f2f2"/></svg>555-210-4876
      </div>
      <div class="contact-line">
        <svg viewBox="0 0 12 12"><rect x="3" y="0.5" width="6" height="11" rx="1" fill="none" stroke="#f2f2f2" stroke-width="1.2"/></svg>555-317-9042
      </div>
      <div class="contact-line">
        <svg viewBox="0 0 12 12"><rect x="0.5" y="2" width="11" height="8" fill="#f2f2f2"/><path d="M1 2.5l5 4 5-4" fill="none" stroke="#232323" stroke-width="1.2"/></svg>info@talbrinhomes.com
      </div>
      <div class="contact-line">
        <svg viewBox="0 0 12 12"><circle cx="6" cy="6" r="5.2" fill="none" stroke="#f2f2f2" stroke-width="1.2"/><path d="M1 6h10M6 1c-2 3-2 7 0 10M6 1c2 3 2 7 0 10" fill="none" stroke="#f2f2f2" stroke-width="0.9"/></svg>www.talbrinhomes.com
      </div>
    </div>
  </section>
  <section class="card card-back">
    <span class="brand-name">Talbrin Homes</span>
  </section>
</main>
</body>
</html>
```